Accounting & Tax Services in Edmonton, Canada-Needs Website Design & Improvement

I am starting my business for accounting and tax services in Canada. I have my website but not much happy with that. My services are for bookkeeping, accounting and tax services. We serve both individual and corporate clients. I am trying to bring new idea in the market for providing services at their facility or business. My existing website is www.kvrm.ca
Currently, this site is static but I want to improve it to dynamic or interactive in nature.

Target Market(s)

Edmonton and Surrounding Areas, Canada

Industry/Entity Type

Public Accounting

Logo Text

Lakeshore Ledger & Office Partners

Number of Pages Required

4 page

Font styles to use
Sans Serif

Colors

Designer to choose colors to be used in the design.

Requirements
Must have
• 4 Pages
• I a not sure what do we mean by coded and uncoded design. Need clarification
• Rest is explained in project description. It should have the ingredients to attract traffic in any professional website.
• Logo Design Text can be shortened, if required.
• Existing logo attached, just for reference.
Nice to have
• 5 Pages

```html
<!DOCTYPE html>
<html lang="en">
<head>
<meta charset="utf-8">
<title>Lakeshore Ledger &amp; Office Partners</title>
<link rel="stylesheet" href="https://fonts.googleapis.com/css2?family=Noto+Serif:wght@400;700&display=swap">
<style>
:root{
  --ink:#3f3f3f;
  --muted:#6a6a6a;
  --brand:#1f5a7a;
  --teal:#3a8fa8;
  --teal-dark:#2c6f85;
  --line:#dcdcdc;
  --band:#f4f4f4;
  --white:#ffffff;
  --hero-a:#2f3438;
  --hero-b:#5b6670;
}
*{margin:0;padding:0;box-sizing:border-box}
html,body{width:1200px;height:2651px;overflow:hidden}
body{position:relative;background:var(--white);color:var(--ink);font-family:"Noto Serif",Georgia,serif}
.abs{position:absolute}
/* header */
.site-header{left:0;top:0;width:1200px;height:143px;background:var(--white)}
.brand{left:100px;top:44px;display:flex;align-items:center;gap:14px}
.brand-mark{width:26px;height:26px;background:var(--brand)}
.brand-name{font-size:24px;color:var(--brand);line-height:1.15;width:260px}
.main-nav{right:97px;top:82px;display:flex;gap:30px;font-size:14px}
.main-nav a{color:var(--brand);text-decoration:none}
/* hero */
.hero{left:0;top:143px;width:1200px;height:478px;background:linear-gradient(135deg,var(--hero-a),var(--hero-b) 55%,#3c4248)}
.hero-text{left:0;top:182px;width:1200px;text-align:center;color:var(--white)}
.hero-title{font-size:50px;font-weight:400;letter-spacing:1px;line-height:1}
.hero-sub{font-size:29px;font-weight:700;margin-top:10px}
.btn{display:inline-block;background:var(--teal);color:var(--white);font-weight:700;text-decoration:none;border-bottom:3px solid var(--teal-dark)}
.hero-btn{left:527px;top:441px;width:146px;height:48px;line-height:45px;text-align:center;font-size:19px}
.hero-arrows{left:568px;top:527px;display:flex;gap:34px}
/* services */
.services{left:0;top:621px;width:1200px;height:435px;background:var(--band)}
.section-title{width:1200px;left:0;text-align:center;font-weight:400;letter-spacing:1px;color:var(--ink)}
.services .section-title{top:56px;font-size:28px}
.connector{left:280px;top:100px}
.service{top:173px;width:260px;text-align:center}
.service-icon{width:84px;height:84px;margin:0 auto;border-radius:10px}
.service h3{font-weight:400;font-size:20px;letter-spacing:1px;margin-top:14px}
.service p{font-size:13px;line-height:19px;color:var(--muted);margin-top:10px;padding:0 12px}
/* about */
.about{left:0;top:1056px;width:1200px;height:434px;background:var(--white)}
.about-photo{left:0;top:0;width:587px;height:434px;background:linear-gradient(140deg,#e9e4dc,#b9ad9c 60%,#8e8070)}
.about-copy{left:629px;top:30px;width:470px}
.about-copy h2{font-weight:400;font-size:27px;letter-spacing:1px}
.about-copy p{font-size:12.5px;line-height:21px;text-align:justify;color:var(--muted);margin-top:12px}
.about-copy p+p{margin-top:20px}
.about-btn{margin-top:18px;width:113px;height:38px;line-height:35px;text-align:center;font-size:14px}
/* tax alerts */
.alerts{left:0;top:1490px;width:1200px;height:400px;background:var(--band)}
.alerts .section-title{top:56px;font-size:23px}
.alert{top:122px;width:294px}
.alert h4{font-size:12px;line-height:19px;font-weight:700;text-transform:uppercase;letter-spacing:.3px;color:#4a4a4a;height:56px}
.alert p{font-size:12.5px;line-height:20px;text-align:justify;color:var(--muted)}
.dots{left:0;width:1200px;display:flex;justify-content:center;gap:9px}
.dot{width:8px;height:8px;background:#9a9a9a;transform:rotate(45deg)}
.dot.on{background:#5a5a5a}
/* testimonials */
.testimonials{left:0;top:1890px;width:1200px;height:405px;background:var(--white)}
.testimonials .section-title{top:56px;font-size:23px}
.quote{top:145px;width:260px}
.avatar{width:66px;height:66px;border-radius:50%}
.quote .who{margin-top:20px;font-size:15px}
.who small{font-size:11px;color:var(--muted)}
.quote p{font-size:12.5px;line-height:20px;color:var(--muted);margin-top:8px}
/* footer */
.site-footer{left:0;top:2295px;width:1200px;height:356px;background:var(--band)}
.foot-brand{left:97px;top:40px;width:190px}
.foot-brand .brand-name{font-size:15px;width:auto}
.foot-brand p{font-size:12px;line-height:19px;color:#888;margin-top:12px}
.foot-col{top:74px;width:230px}
.foot-col h5{font-size:15px;font-weight:400;color:#222}
.foot-col p,.foot-col li{font-size:12px;line-height:19px;color:#888}
.foot-col ul{list-style:none;margin-top:18px}
.foot-col li{margin-bottom:7px}
.foot-col .when{color:#c8c8c8;margin-top:10px}
.news-form{margin-top:24px;display:flex;width:232px;height:40px}
.news-input{flex:1;border:1px solid var(--teal);background:var(--white);font-size:12px;color:#888;padding:0 14px;line-height:38px}
.news-btn{width:86px;background:var(--brand);color:var(--white);font-size:12px;text-align:center;line-height:40px}
.foot-rule{left:97px;top:268px;width:1006px;height:1px;background:#e4e4e4}
.copyright{left:113px;top:302px;font-size:12px;color:#999}
.foot-nav{right:97px;top:302px;display:flex;gap:38px;font-size:12px}
.foot-nav a{color:#222;text-decoration:none}
</style>
</head>
<body>

<header class="site-header abs">
  <div class="brand abs">
    <span class="brand-mark"></span>
    <span class="brand-name">Lakeshore Ledger &amp; Office Partners</span>
  </div>
  <nav class="main-nav abs">
    <a href="#">Home</a><a href="#">About Us</a><a href="#">Services</a><a href="#">Contact Us</a>
  </nav>
</header>

<section class="hero abs" role="img" aria-label="Top-down photo of a team working with laptops and documents at a white desk"></section>
<div class="hero-text abs" style="top:325px">
  <h1 class="hero-title">WE ARE AN</h1>
  <p class="hero-sub">accounting and tax services in Canada</p>
</div>
<a class="btn hero-btn abs" href="#">Learn More</a>
<div class="hero-arrows abs">
  <svg width="14" height="22" viewBox="0 0 14 22"><path d="M11 2 3 11l8 9" fill="none" stroke="#fff" stroke-width="3"/></svg>
  <svg width="14" height="22" viewBox="0 0 14 22"><path d="M3 2l8 9-8 9" fill="none" stroke="#fff" stroke-width="3"/></svg>
</div>

<section class="services abs">
  <h2 class="section-title abs">Our Services</h2>
  <svg class="connector abs" width="640" height="60" viewBox="0 0 640 60">
    <path d="M320 0v36M0 60V36h640v24" fill="none" stroke="#d8d8d8" stroke-width="1"/>
  </svg>
  <div class="service abs" style="left:150px">
    <div class="service-icon" role="img" aria-label="Bookkeeping ledger icon" style="background:#3ba3d8"></div>
    <h3>Bookkeeping</h3>
    <p>sed do eiusmod tempor incididunt uto labore dolore magna aliqua enim minim veniam.</p>
  </div>
  <div class="service abs" style="left:470px">
    <div class="service-icon" role="img" aria-label="Accounting coins icon" style="background:#f2c81c;border-radius:50%"></div>
    <h3>Accounting</h3>
    <p>sed do eiusmod tempor incididunt uto labore dolore magna aliqua enim minim veniam.</p>
  </div>
  <div class="service abs" style="left:790px">
    <div class="service-icon" role="img" aria-label="Tax document and pencil icon" style="background:#6fc7b5"></div>
    <h3>Tax Services</h3>
    <p>sed do eiusmod tempor incididunt uto labore dolore magna aliqua enim minim veniam.</p>
  </div>
</section>

<section class="about abs">
  <div class="about-photo abs" role="img" aria-label="Hands writing notes beside a calculator, coffee cup and glasses on a wooden desk"></div>
  <div class="about-copy abs">
    <h2>About Us</h2>
    <p>Welcome and thank you for visiting our website. At Lakeshore Ledger &amp; Office Partners, we have built our business so that it guarantees your success. In addition to providing you with a profile of our firm and the services we provide, this website has been designed to become a helpful resource tool to you, our valued clients and visitors.</p>
    <p>Our firm endeavors to provide you with the highest quality of service and we hope that you find the information on this website useful. For any additional questions or comments please do not hesitate to contact us. We will get back to you as soon as possible as we pride ourselves on being proactive and responsive to our clients' inquiries and suggestions.</p>
    <a class="btn about-btn" href="#">Read More</a>
  </div>
</section>

<section class="alerts abs">
  <h2 class="section-title abs">TAX ALERTS</h2>
  <article class="alert abs" style="left:118px">
    <h4>Northern Reserve Bank leaves interest rates unchanged</h4>
    <p>As expected, the Northern Reserve Bank made no change to current interest rates in its announcement made on December 7. Consequently, the bank rate remains at 0.75%. In its announcement, which can be found ...</p>
  </article>
  <article class="alert abs" style="left:454px">
    <h4>Unemployment rate down slightly in November</h4>
    <p>The most recent release of National Data Bureau's Labour Force Survey shows that the overall unemployment rate declined slightly during November, dropping from 7% to 6.8%. During November, employm...</p>
  </article>
  <article class="alert abs" style="left:790px">
    <h4>FRO webinar on payroll deductions for businesses</h4>
    <p>The Federal Revenue Office (FRO) regularly holds webinars for businesses on how to fulfill their payroll reporting and remittance obligations. The last in the current series of such webinars, which wi...</p>
  </article>
  <div class="dots abs" style="top:321px"><span class="dot on"></span><span class="dot"></span><span class="dot on"></span></div>
</section>

<section class="testimonials abs">
  <h2 class="section-title abs">TESTIMONIALS</h2>
  <div class="quote abs" style="left:155px">
    <div class="avatar" role="img" aria-label="Portrait of David Doe" style="background:#a58a78"></div>
    <p class="who">David Doe <small>/ Manager</small></p>
    <p>Duis aute irure dolor in reprehenderit in voluptate velit esse cillum dolore eu fugiat nulla pariatur sint occaecat cupidatat.</p>
  </div>
  <div class="quote abs" style="left:473px">
    <div class="avatar" role="img" aria-label="Portrait of Juliana" style="background:#c08a6c"></div>
    <p class="who">Juliana <small>/ UI Designer</small></p>
    <p>Duis aute irure dolor in reprehenderit in voluptate velit esse cillum dolore eu fugiat nulla pariatur sint occaecat cupidatat.</p>
  </div>
  <div class="quote abs" style="left:792px">
    <div class="avatar" role="img" aria-label="Portrait of Hisuma" style="background:#b07a66"></div>
    <p class="who">Hisuma <small>/ SEO Expert</small></p>
    <p>Duis aute irure dolor in reprehenderit in voluptate velit esse cillum dolore eu fugiat nulla pariatur sint occaecat cupidatat.</p>
  </div>
  <div class="dots abs" style="top:366px;gap:20px"><span class="dot on"></span><span class="dot on"></span><span class="dot on"></span><span class="dot on"></span></div>
</section>

<footer class="site-footer abs">
  <div class="foot-brand abs">
    <span class="brand-name">Lakeshore Ledger &amp; Office Partners</span>
    <p>consequuntur magni dolores atione voluptatem sequi nesc ue porro quisquam est, qui d sum quia dolor sit amet,cons sum quia sum quia</p>
  </div>
  <div class="foot-col abs" style="left:355px">
    <h5>Contact</h5>
    <ul>
      <li>www.loremipsumdolar.nl</li>
      <li>182 AB Your Street Name</li>
      <li>e-mail@loremipsum.com</li>
      <li>+(121) 01 23 45 679</li>
    </ul>
  </div>
  <div class="foot-col abs" style="left:611px;width:175px">
    <h5>Latest Tweet</h5>
    <p style="margin-top:18px">"...aerat vluptatem. Ut eni et illi dolore magnam aliqua et aerat voluptatem. Utils eni tils et al is minima veniam."</p>
    <p class="when">3 hours ago</p>
  </div>
  <div class="foot-col abs" style="left:868px;width:235px">
    <h5>Newsletter</h5>
    <p style="margin-top:18px">Neque porro quisquam eist, im ipsum quia dolor sit ametur, adipisci velit,</p>
    <div class="news-form"><span class="news-input">E-mail address</span><span class="news-btn">Subscribe</span></div>
  </div>
  <div class="foot-rule abs"></div>
  <p class="copyright abs">© 2017 &nbsp;|&nbsp; www.companyname.com</p>
  <nav class="foot-nav abs"><a href="#">Home</a><a href="#">About</a><a href="#">Services</a><a href="#">Contact Us</a></nav>
</footer>

</body>
</html>
```